Business Cards for a unique Russian patisserie

VOLTA Russian Treats bakery intends to introduce Australian public to amazing Russian pastries and traditions of genuine Russian hospitality.
VOLTA business model is a café, selling a mix of Russian, Eastern European and traditional pastries produced in-house.
VOLTA’s ultimate goal is to create a superior eating experience and to become a destination eatery in Sydney.
I would like the business cards match our ambitious purpose, to be unique and bold. I want them to be sophisticated (as opposed to straightforward and tacky) and graphical. I would love if Russian national ornament (hohloma) elements to be used.
Dominating colours - red and black. For the styling guide please see our logo attached.
Target Market(s)
Business partners, suppliers, possible corporate clients
Industry/Entity Type
Bakery

```html
<!DOCTYPE html>
<html lang="en">
<head>
<meta charset="utf-8">
<title>VOLTA Russian Treats – Business Cards</title>
<link rel="stylesheet" href="https://fonts.googleapis.com/css2?family=Open+Sans:wght@400;600;700;800&display=swap">
<style>
  :root{
    --backdrop:#e9e5e0;
    --card-white:#ffffff;
    --brown:#35261d;
    --red:#e3262e;
    --ink:#231f20;
    --grey-rule:#b9b9b9;
    --cream:#ffffff;
  }
  *{box-sizing:border-box;margin:0;padding:0}
  html,body{width:1200px;height:1177px;overflow:hidden}
  body{background:var(--backdrop);position:relative;font-family:"Open Sans",Arial,sans-serif}

  .card{position:absolute;border-radius:30px;overflow:hidden;box-shadow:0 4px 14px rgba(0,0,0,.18)}
  .card-front{left:28px;top:38px;width:921px;height:527px;background:var(--card-white)}
  .card-back{left:246px;top:617px;width:918px;height:523px;background:var(--brown)}

  .front-bands{position:absolute;inset:0}

  .brand-lockup{position:absolute;left:120px;top:100px;width:360px;text-align:center;color:var(--brown)}
  .brand-dot{width:120px;height:120px;border-radius:50%;background:var(--red);margin:0 auto 22px}
  .brand-name{font-weight:800;font-size:72px;line-height:1;letter-spacing:3px}
  .brand-tagline{font-weight:800;font-size:22px;line-height:1.3;color:var(--brown)}

  .divider{position:absolute;left:513px;top:100px;width:2px;height:250px;background:var(--grey-rule)}

  .contact-block{position:absolute;left:562px;top:98px}
  .person-name{color:var(--red);font-weight:600;font-size:30px;line-height:1.2}
  .person-title{color:var(--ink);font-size:22px;line-height:1.3;margin-bottom:20px}
  .contact-list{list-style:none}
  .contact-list li{display:flex;align-items:center;gap:10px;font-size:22px;line-height:37px;color:var(--ink)}
  .contact-list svg{width:18px;height:18px;fill:var(--red);flex:none}

  .address{position:absolute;left:0;width:960px;top:481px;text-align:center;color:var(--cream);font-size:21px;font-weight:600;line-height:28px}

  .back-brand{position:absolute;left:0;right:0;top:150px;text-align:center;color:var(--red);font-weight:800;font-size:120px;line-height:1;letter-spacing:6px}
  .back-tagline{position:absolute;left:0;right:0;top:285px;text-align:center;color:var(--red);font-weight:800;font-size:30px}
  .back-web{position:absolute;left:0;right:0;top:445px;text-align:center;color:var(--cream);font-size:28px;letter-spacing:5px}
</style>
</head>
<body>
  <section class="card card-front">
    <svg class="front-bands" viewBox="0 0 921 527" width="921" height="527" aria-hidden="true">
      <path d="M0 346 C250 440 560 462 760 448 C560 466 250 452 0 372 Z" fill="var(--red)"/>
      <path d="M0 384 C250 470 600 495 921 440 L921 527 L0 527 Z" fill="var(--brown)"/>
    </svg>

    <div class="brand-lockup">
      <div class="brand-dot"></div>
      <div class="brand-name">VOLTA</div>
      <div class="brand-tagline">Russian Treats</div>
    </div>

    <div class="divider"></div>

    <div class="contact-block">
      <div class="person-name">Your Name</div>
      <div class="person-title">Title</div>
      <ul class="contact-list">
        <li><svg viewBox="0 0 20 20"><path d="M5 2l3 4-2 2c1 3 3 5 6 6l2-2 4 3-2 3C9 18 2 11 2 4z"/></svg>012-345-6789</li>
        <li><svg viewBox="0 0 20 20"><path d="M2 14h16v-4l-2-4H4l-2 4zM5 15a2 2 0 1 0 0 .1zM15 15a2 2 0 1 0 0 .1z"/></svg>012-345-6789</li>
        <li><svg viewBox="0 0 20 20"><path d="M2 5h16v11H2zM2 5l8 6 8-6" stroke="#fff" stroke-width="1.2"/></svg>info@voltatreats.com</li>
        <li><svg viewBox="0 0 20 20"><circle cx="10" cy="10" r="8"/><path d="M2 10h16M10 2c-4 4-4 12 0 16M10 2c4 4 4 12 0 16" stroke="#fff" stroke-width="1.2" fill="none"/></svg>www.voltatreats.com</li>
      </ul>
    </div>

    <div class="address">Street Name, City Name, Zip Code-00000</div>
  </section>

  <section class="card card-back">
    <div class="back-brand">VOLTA</div>
    <div class="back-tagline">Russian Treats</div>
    <div class="back-web">www.voltatreats.com</div>
  </section>
</body>
</html>
```